2 Fold Brochure

We are a spa looking to create a professional elegant two fold brochure for a spa mainly black and white with a splash of lime green.
Look and feel: chic, modern, and spa-ish.

The front will include an image and also it should say: (somewhere under the photo) wherever you think it will look nice.
Skin Tightening
Cellulite Reduction
Body Contouring

The second Page:
Bipolar Radiofrequency(bolded): for immediate face lifting, tone and a complete new younger looking skin!
Multipolar Radiofrequency(bolded): with Vacuum system for body contour, cellulite and fat detachment from adipose tissue.
Cavitation with red LED to treat face and small areas of the body. Red LED light stimulates collagen synthesis.

Ultra Cavitation will sculpt, treat fat, cellulite and improve body shape! It does NOT involve surgery. There is no need for anesthesia, hospital stay or time off from work. Ultra cavitation will promote microscopic air bubbles to surround the lipocyte(fat cell) membranes and with its resonant frequency, the bubbles cause a high enough pressure to break up fat instantly. These broken lipocytes are then safely metabolized out of the human body.

PRESSOTHERAPY: A Complete Body Detox! Pressortherapy based on air pressure, promotes lymphatic drainage. It aslo has infrared system for body heat and electro muscle stimulation system.

Third Page:
Packages:

1. THE NEW FACELIFT:
*Skin Tightening
*Wrinkle Reduction
*Dark Circle Elimination
*Puffy Eye Relief

BODY SHAPING

2. BODY
*Fat Reduction
*Cellulite Reduction
*Body Firming

3. PRESSOTHERAPY (DETOX) $85
*Toxic Flushing
*Lymphatic Drainage
*Toning

5.POST PREGNANCY
*Fat Reduction
*Tummy Firming and Toning
*Cellulite Reduction
*Butt Toning

Buy 5 get 1 Free - $1,250
Buy 10 get 2 Free- $2,500

The back of the second page will include before and after photos I will be sending later. Also include the Logo in the front and by the prices. I have attached our logo.

Also we need a photo to place in the front. Something that shows face and body fat reduction.

Industry/Entity Type

Hospital

```html
<!DOCTYPE html>
<html lang="en">
<head>
<meta charset="utf-8">
<title>Luma Day Spa – Treatments &amp; Packages</title>
<link rel="stylesheet" href="https://fonts.googleapis.com/css2?family=Arimo:wght@400;700&family=Handlee&display=swap">
<style>
  :root {
    --ink: #000000;
    --paper: #ffffff;
    --lime: #bcd534;
    --mist: #eef0ea;
    --skin-light: #efe2d4;
    --skin-warm: #d8b494;
    --sky: #cfe0ee;
    --sky-deep: #8fb3d1;
  }
  * { box-sizing: border-box; margin: 0; padding: 0; }
  html, body {
    width: 990px; height: 1200px; overflow: hidden;
    background: var(--paper);
  }
  .brochure {
    position: relative; width: 990px; height: 1200px;
    font-family: "Arimo", Arial, sans-serif; color: var(--paper);
  }
  .script { font-family: "Handlee", cursive; font-weight: 400; }

  .treatments {
    position: absolute; left: 0; top: 0; width: 495px; height: 1013px;
    background: var(--ink); text-align: center; padding: 40px 44px 0;
  }
  .treatments h2 { font-size: 38px; line-height: 1.2; margin-bottom: 6px; }
  .treatments p { font-size: 16.5px; line-height: 20.5px; }
  .treatments p + p { margin-top: 20.5px; }
  .treatments .gap-lg { margin-top: 34px; }
  .treatments .gap-xl { margin-top: 52px; }

  .photo-hero {
    position: absolute; left: 495px; top: 0; width: 495px; height: 303px;
    background: linear-gradient(100deg, var(--paper) 0%, var(--mist) 35%, var(--skin-light) 65%, var(--skin-warm) 100%);
  }

  .packages-band {
    position: absolute; left: 478px; top: 303px; width: 512px; height: 80px;
    background: var(--lime); text-align: center;
  }
  .packages-band h2 { font-size: 56px; line-height: 80px; color: var(--paper); }

  .packages {
    position: absolute; left: 495px; top: 383px; width: 495px; height: 630px;
    background: var(--ink); text-align: center; padding-top: 32px;
    font-size: 16.5px; line-height: 20.5px;
  }
  .packages .pkg-title { font-weight: 700; }
  .packages .pkg + .pkg { margin-top: 20px; }
  .packages h3 { font-size: 38px; line-height: 1.2; margin: 36px 0 20px; }

  .photo-relax {
    position: absolute; left: 0; top: 1013px; width: 495px; height: 187px;
    background: linear-gradient(90deg, var(--sky) 0%, var(--paper) 35%, var(--skin-light) 60%, var(--sky-deep) 100%);
  }

  .offers {
    position: absolute; left: 495px; top: 1013px; width: 495px; height: 187px;
    background: var(--lime); color: var(--ink); padding: 36px 0 0 58px;
  }
  .offers p { font-size: 38px; line-height: 58px; }

  .brand-seal {
    position: absolute; left: 427px; top: 910px; width: 172px; height: 172px;
    border-radius: 50%; background: var(--paper); border: 5px solid var(--ink);
    display: flex; align-items: center; justify-content: center; text-align: center;
    color: var(--ink); font-family: "Arimo", Arial, sans-serif; font-size: 20px; line-height: 24px;
  }
</style>
</head>
<body>
<main class="brochure">

  <section class="treatments">
    <h2 class="script">Bipolar Radiofrequency</h2>
    <p>for immediate face lifting, tone and a<br>complete new younger looking skin!</p>

    <h2 class="script gap-lg">Multipolar Radiofrequency</h2>
    <p>with Vacuum system for body contour,<br>cellulite and fat detachment from<br>adipose tissue.</p>
    <p>Cavitation with red LED to treat face and<br>small areas of the body. Red LED light<br>stimulates collagen synthesis.</p>
    <p>Ultra Cavitation will sculpt, treat fat,<br>cellulite and improve body shape!<br>It does NOT involve surgery. There is<br>no need for anesthesia, hospital stay<br>or time off from work. Ultra cavitation<br>will promote microscopic air bubbles<br>to surround the lipocyte(fat cell)<br>membranes and with its resonant<br>frequency, the bubbles cause a high<br>enough pressure to break up fat instantly.<br>These broken lipocytes are then safely<br>metabolized out of the human body.</p>

    <h2 class="script gap-xl">Pressotherapy</h2>
    <p>A Complete Body Detox!<br>Pressortherapy based on air pressure,<br>promotes lymphatic drainage. It aslo<br>has infrared system for body heat and<br>electro muscle stimulation system.</p>
  </section>

  <div class="photo-hero" role="img" aria-label="Photo of a slim waist in a lime green bikini"></div>

  <div class="packages-band"><h2 class="script">Packages</h2></div>

  <section class="packages">
    <div class="pkg">
      <p class="pkg-title">1. THE NEW FACELIFT:</p>
      <p>*Skin Tightening<br>*Wrinkle Reduction<br>*Dark Circle Elimination<br>*Puffy Eye Relief</p>
    </div>

    <h3 class="script">Body Shaping</h3>

    <div class="pkg">
      <p class="pkg-title">2. BODY</p>
      <p>*Fat Reduction<br>*Cellulite Reduction<br>*Body Firming</p>
    </div>
    <div class="pkg">
      <p class="pkg-title">3. PRESSOTHERAPY (DETOX) $85</p>
      <p>*Toxic Flushing<br>*Lymphatic Drainage<br>*Toning</p>
    </div>
    <div class="pkg">
      <p class="pkg-title">5.POST PREGNANCY</p>
      <p>*Fat Reduction<br>*Tummy Firming and Toning<br>*Cellulite Reduction<br>*Butt Toning</p>
    </div>
  </section>

  <div class="photo-relax" role="img" aria-label="Photo of a relaxed woman at the spa holding a white flower"></div>

  <section class="offers">
    <p class="script">Buy 5 get 1 Free - $1,250</p>
    <p class="script">Buy 10 get 2 Free- $2,500</p>
  </section>

  <div class="brand-seal">Luma<br>Day Spa</div>

</main>
</body>
</html>
```